We're Hiring Poster or Flyer design

We’re Hiring Details:

Positions include:
Office Manager
Office Assistant
Data Entry Techs
Outreach Manager
Asst. Outreach Manager
Events Coordinator
Drivers (must have personal car, insurance & Driver’s License)
Outreach Specialist—Walkers
Outreach Specialist—Phone/Telemarketing (evenings only)

Excellent Pay ! Fun Atmosphere ! Bonus Pay with Promotional & Career Advancement Opportunities

***************
need 3 formats of SAME flyer:
1) 8.5 x 11
2) 8.5 x 14
3) 11 x17

creative and eye catching a must; this flyer will be used on college bulletin boards and used to attract a younger demographic . . hip and chic look with "Americana style or political motif" preferred.

Target Market(s)

younger demographic . . flyer will be used during college recruiting fairs and in younger settings---age BRACKET is 21 - 35 Years old

Industry/Entity Type

Employment Agency

Font styles to use
Sans Serif

Colors

Designer to choose colors to be used in the design.

Requirements
Must have
• clean and attractive; hip; chic; simple and with good stock pics and layout
Nice to have
• american flag and patriotism
Should not have
• too much details on the job -- I only included the job announcement so you can get an idea of WHAT and WHO I am looking for . . don't list all the BORING details on the flyer/poster

```html
<!DOCTYPE html>
<html lang="en">
<head>
<meta charset="utf-8">
<title>We're Hiring – Marco Castellan for Mayor</title>
<link rel="stylesheet" href="https://fonts.googleapis.com/css2?family=Open+Sans:wght@600;700;800&family=Roboto+Condensed:wght@400;700&family=Roboto:wght@900&display=swap">
<style>
  :root {
    --navy: #123a78;
    --navy-deep: #0d2f66;
    --red: #e8231f;
    --orange: #f26522;
    --yellow: #f6c51a;
    --yellow-dark: #d9a70b;
    --paper: #f3f3f2;
    --ink: #1d1d1f;
    --white: #ffffff;
  }
  * { margin: 0; padding: 0; box-sizing: border-box; }
  html, body { width: 998px; height: 1200px; overflow: hidden; background: #e9e9e9; }
  .poster {
    position: relative;
    width: 998px;
    height: 1200px;
    background: linear-gradient(180deg, #f7f7f6 0%, var(--paper) 100%);
    font-family: "Open Sans", sans-serif;
    overflow: hidden;
  }

  /* Header */
  .brand {
    position: absolute;
    left: 52px; top: 50px;
    width: 200px;
    display: flex; align-items: center; gap: 10px;
  }
  .brand-dot { width: 14px; height: 14px; border-radius: 50%; background: var(--orange); flex: none; }
  .brand-name {
    font-weight: 800; font-size: 30px; line-height: 1.05; color: var(--navy);
  }
  .perks {
    position: absolute;
    left: 258px; top: 58px; width: 710px;
  }
  .perks-main {
    height: 42px;
    background: var(--red);
    color: var(--white);
    font-family: "Open Sans", sans-serif;
    font-weight: 700; font-size: 21px;
    display: flex; align-items: center; justify-content: center; gap: 14px;
  }
  .perks-main .sep { width: 7px; height: 7px; border-radius: 50%; background: var(--navy-deep); }
  .perks-sub {
    height: 44px;
    background: var(--navy);
    color: var(--white);
    font-family: "Roboto Condensed", sans-serif;
    font-size: 24px;
    display: flex; align-items: center; justify-content: center;
    border-top: 3px solid var(--white);
  }

  /* Photo */
  .team-photo {
    position: absolute;
    left: 22px; top: 168px; width: 954px; height: 452px;
    background: linear-gradient(180deg, #a7c58e 0%, #d8e4c6 38%, #c9a47e 70%, #7f9cc4 100%);
  }
  .photo-rule {
    position: absolute; left: 22px; top: 620px; width: 954px; height: 8px;
    background: var(--orange);
  }

  /* Hiring badge */
  .hiring-badge {
    position: absolute;
    left: 672px; top: 500px;
    width: 238px; height: 238px;
    border-radius: 50%;
    background: var(--navy);
    border: 9px solid var(--white);
    box-shadow: 0 0 0 3px var(--orange);
    display: flex; flex-direction: column; align-items: center; justify-content: center;
    font-family: "Roboto", sans-serif; font-weight: 900;
    color: var(--orange);
    line-height: 1.05;
  }
  .hiring-badge .we { font-size: 44px; }
  .hiring-badge .hiring { font-size: 48px; }

  /* Positions tab */
  .positions-tab {
    position: absolute;
    left: 78px; top: 616px;
    width: 214px; height: 70px;
  }
  .positions-tab svg { position: absolute; inset: 0; }
  .positions-tab span {
    position: relative; display: block;
    padding-top: 14px; text-align: center;
    font-weight: 700; font-size: 23px; color: var(--ink);
  }

  /* Positions list */
  .positions {
    position: absolute; left: 84px; top: 712px; width: 880px;
    list-style: none;
  }
  .positions li {
    position: absolute;
    display: flex; align-items: center; gap: 12px;
    font-weight: 700; font-size: 20px; color: var(--ink);
    white-space: nowrap;
  }
  .tick { width: 20px; height: 20px; flex: none; }

  /* Flag + footer */
  .flag-wash {
    position: absolute; left: 0; top: 960px; width: 998px; height: 150px;
    background: linear-gradient(90deg, rgba(120,130,210,.28) 0%, rgba(170,190,240,.2) 35%, rgba(240,150,190,.22) 60%, rgba(240,170,200,.18) 100%);
  }
  .footer {
    position: absolute; left: 0; top: 1080px; width: 998px; height: 120px;
  }
  .footer svg { position: absolute; inset: 0; }
  .footer-url {
    position: absolute; left: 0; right: 0; top: 62px;
    text-align: center;
    color: var(--white);
    font-weight: 600; font-size: 16px; letter-spacing: 6px;
  }
</style>
</head>
<body>
<main class="poster">

  <header>
    <div class="brand">
      <span class="brand-dot"></span>
      <span class="brand-name">Marco<br>Castellan</span>
    </div>
    <div class="perks">
      <div class="perks-main">
        <span>Excellent Pay !</span><span class="sep"></span>
        <span>Fun Atmosphere !</span><span class="sep"></span>
        <span>Bonus Pay</span>
      </div>
      <div class="perks-sub">with Promotional &amp; Career Advancement Opportunities</div>
    </div>
  </header>

  <div class="team-photo" role="img" aria-label="Photo of five smiling young adults sitting together outdoors under green trees, one holding a laptop"></div>
  <div class="photo-rule"></div>

  <div class="hiring-badge">
    <span class="we">We’re</span>
    <span class="hiring">HIRING</span>
  </div>

  <div class="positions-tab">
    <svg viewBox="0 0 214 70" preserveAspectRatio="none" aria-hidden="true">
      <path d="M0 0 H214 V48 L107 70 L0 48 Z" fill="var(--yellow)"/>
      <path d="M0 0 H214 V6 H0 Z" fill="var(--yellow-dark)"/>
    </svg>
    <span>Positions are</span>
  </div>

  <svg width="0" height="0" style="position:absolute">
    <symbol id="tick" viewBox="0 0 20 20">
      <circle cx="10" cy="10" r="8.2" fill="none" stroke="var(--navy)" stroke-width="2"/>
      <path d="M6 10.2 L9 13 L14.2 7.2" fill="none" stroke="var(--navy)" stroke-width="2.2" stroke-linecap="round" stroke-linejoin="round"/>
    </symbol>
  </svg>

  <ul class="positions">
    <li style="left:0;top:0"><svg class="tick"><use href="#tick"/></svg>Office Manager</li>
    <li style="left:260px;top:0"><svg class="tick"><use href="#tick"/></svg>Office Assistant</li>
    <li style="left:0;top:60px"><svg class="tick"><use href="#tick"/></svg>Data Entry Techs</li>
    <li style="left:260px;top:60px"><svg class="tick"><use href="#tick"/></svg>Outreach Manager</li>
    <li style="left:520px;top:60px"><svg class="tick"><use href="#tick"/></svg>Asst. Outreach Manager</li>
    <li style="left:0;top:120px"><svg class="tick"><use href="#tick"/></svg>Events Coordinator</li>
    <li style="left:260px;top:120px"><svg class="tick"><use href="#tick"/></svg>Outreach Specialist—Walkers</li>
    <li style="left:0;top:180px"><svg class="tick"><use href="#tick"/></svg>Drivers (must have personal car, insurance &amp; Driver’s License)</li>
    <li style="left:0;top:240px"><svg class="tick"><use href="#tick"/></svg>Outreach Specialist—Phone/Telemarketing (evenings only)</li>
  </ul>

  <div class="flag-wash" role="img" aria-label="Faded American flag with stars and stripes waving across the lower section"></div>

  <footer class="footer">
    <svg viewBox="0 0 998 120" preserveAspectRatio="none" aria-hidden="true">
      <path d="M0 14 L80 6 L160 18 L260 4 L360 16 L470 2 L580 14 L690 0 L790 12 L890 2 L998 10 V120 H0 Z" fill="var(--white)"/>
      <path d="M0 40 L60 30 L120 44 L200 28 L290 38 L380 24 L470 36 L560 22 L650 34 L740 20 L830 32 L920 22 L998 30 V120 H0 Z" fill="var(--navy)"/>
    </svg>
    <div class="footer-url">WWW.CASTELLANFORMAYOR.COM</div>
  </footer>

</main>
</body>
</html>
```